hotel amenities supply company needs design for bottles and accessories

we need to design four 30ml amenity tubes branded "VELORA" , shampoo, shower gel, conditioner and body lotion. the bottle has to be somewhat clear to be able to see the liquid inside. its basically designing the complete identity for "velora". attached are some examples. also the accessory boxes should match the design eg, shaving kit,vanity kit, toothbrush etc

Target Market(s)

hotels

Industry/Entity Type

Hotel

Font styles to use
Script

Requirements
Must have
• name "velora " on bottles and product info
Should not have
• dark colors

```html
<!DOCTYPE html>
<html lang="en">
<head>
<meta charset="utf-8">
<title>Velora Amenity Tubes</title>
<link rel="stylesheet" href="https://fonts.googleapis.com/css2?family=Norican&family=Open+Sans:wght@600;700&display=swap">
<style>
  :root {
    --page: #f4fbfd;
    --ink: #141414;
    --ornament: #a29f80;
    --rule: #2a2a2a;
    --green-top: #d6dea4;
    --green-bottom: #e4e8bf;
    --white-top: #efefef;
    --white-bottom: #fafafa;
    --blue-top: #c4e3f6;
    --blue-bottom: #d8eefa;
  }
  * { box-sizing: border-box; margin: 0; padding: 0; }
  html, body { width: 1200px; height: 1200px; overflow: hidden; }
  body {
    background: var(--page);
    font-family: "Open Sans", Arial, sans-serif;
    color: var(--ink);
  }
  .range {
    position: absolute;
    left: 30px;
    top: 210px;
    display: flex;
    gap: 28px;
  }
  .label {
    position: relative;
    width: 264px;
    height: 680px;
    border-radius: 6px;
    overflow: hidden;
  }
  .label--shampoo { background: linear-gradient(180deg, var(--green-top), var(--green-bottom)); }
  .label--conditioner, .label--lotion { background: linear-gradient(180deg, var(--white-top), var(--white-bottom)); box-shadow: inset 0 0 0 1px #e2e2e2; }
  .label--gel { background: linear-gradient(180deg, var(--blue-top), var(--blue-bottom)); }

  .product-name {
    position: absolute;
    left: 86px;
    top: 96px;
    width: 150px;
    text-align: center;
    font-weight: 600;
    font-size: 19px;
    line-height: 26px;
  }
  .product-name .line { display: block; }
  .product-name .line:first-child {
    border-bottom: 2px solid var(--rule);
    margin: 0 14px;
    padding-bottom: 2px;
  }
  .ornament {
    position: absolute;
    left: 166px;
    top: 190px;
    width: 92px;
    height: 400px;
    background: repeating-linear-gradient(180deg, var(--ornament) 0 3px, transparent 3px 14px),
                repeating-linear-gradient(90deg, var(--ornament) 0 3px, transparent 3px 14px);
    opacity: 0.55;
  }
  .brand {
    position: absolute;
    left: -120px;
    top: 325px;
    width: 440px;
    height: 150px;
    line-height: 150px;
    text-align: center;
    font-family: "Norican", cursive;
    font-size: 132px;
    color: var(--ink);
    transform: rotate(-90deg);
  }
  .volume {
    position: absolute;
    left: 0;
    right: 0;
    top: 610px;
    text-align: center;
    font-weight: 700;
    font-size: 19px;
  }
</style>
</head>
<body>
  <main class="range">
    <section class="label label--shampoo">
      <h2 class="product-name"><span class="line">shampoo</span><span class="line">green tea</span></h2>
      <div class="ornament" role="img" aria-label="Vertical band of ornamental arabesque pattern"></div>
      <p class="brand">Velora</p>
      <p class="volume">30 ml / 1 fl. oz.</p>
    </section>
    <section class="label label--conditioner">
      <h2 class="product-name"><span class="line">conditioner</span><span class="line">for hair</span></h2>
      <div class="ornament" role="img" aria-label="Vertical band of ornamental arabesque pattern"></div>
      <p class="brand">Velora</p>
      <p class="volume">30 ml / 1 fl. oz.</p>
    </section>
    <section class="label label--lotion">
      <h2 class="product-name"><span class="line">body lotion</span><span class="line">milk &amp; honey</span></h2>
      <div class="ornament" role="img" aria-label="Vertical band of ornamental arabesque pattern"></div>
      <p class="brand">Velora</p>
      <p class="volume">30 ml / 1 fl. oz.</p>
    </section>
    <section class="label label--gel">
      <h2 class="product-name"><span class="line">shower gel</span><span class="line">ocean fresh</span></h2>
      <div class="ornament" role="img" aria-label="Vertical band of ornamental arabesque pattern"></div>
      <p class="brand">Velora</p>
      <p class="volume">30 ml / 1 fl. oz.</p>
    </section>
  </main>
</body>
</html>
```